PTA Meeting Poster

We are looking to create a poster to invite parents of our school to our monthly PTA Meeting.

The copy should include:

PTA Meeting
This Wednesday
8:40am
in the Multi Purpose Room

All Welcome!

```html
<!DOCTYPE html>
<html lang="en">
<head>
<meta charset="UTF-8">
<title>PTA Meeting Poster</title>
<link href="https://fonts.googleapis.com/css2?family=Paytone+One&family=Montserrat:wght@300;400&family=Caveat:wght@500&display=swap" rel="stylesheet">
<style>
  :root {
    --bg-centre: #fbfdea;
    --bg-mid: #e6f3cf;
    --bg-edge: #b4d994;
    --title-pink: #ff11bd;
    --ink: #111111;
    --marker-red: #e3141b;
  }
  html, body {
    margin: 0;
    padding: 0;
    overflow: hidden;
  }
  .poster {
    position: relative;
    width: 848px;
    height: 1200px;
    overflow: hidden;
    background: radial-gradient(ellipse 70% 62% at 50% 37%, var(--bg-centre) 0%, var(--bg-mid) 45%, var(--bg-edge) 100%);
    color: var(--ink);
    font-family: "Montserrat", sans-serif;
    font-weight: 300;
  }
  .poster-title {
    position: absolute;
    top: 112px;
    left: 0;
    width: 866px;
    margin: 0;
    text-align: center;
    font-family: "Paytone One", sans-serif;
    font-weight: 400;
    font-size: 70px;
    line-height: 1;
    color: var(--title-pink);
  }
  .meeting-details {
    position: absolute;
    top: 286px;
    left: 99px;
    margin: 0;
  }
  .meeting-day,
  .meeting-time {
    display: block;
    font-size: 49px;
    line-height: 49px;
    font-weight: 300;
  }
  .meeting-place {
    display: block;
    margin-top: 14px;
    font-size: 29px;
    line-height: 32px;
    font-weight: 300;
  }
  .calendar {
    position: absolute;
    top: 530px;
    left: 0;
    width: 848px;
    height: 340px;
  }
  .calendar .month {
    font-family: "Caveat", cursive;
    font-size: 32px;
    font-weight: 500;
  }
  .calendar .year {
    font-family: "Montserrat", sans-serif;
    font-size: 27px;
    font-weight: 300;
  }
  .calendar .weekday {
    font-family: "Caveat", cursive;
    font-size: 23px;
    font-weight: 500;
  }
  .calendar .date {
    font-family: "Montserrat", sans-serif;
    font-size: 19px;
    font-weight: 300;
  }
  .welcome {
    position: absolute;
    top: 1010px;
    left: 0;
    width: 862px;
    margin: 0;
    text-align: center;
    font-size: 63px;
    line-height: 1;
    font-weight: 300;
  }
</style>
</head>
<body>
<main class="poster">
  <h1 class="poster-title">PTA Meeting</h1>

  <p class="meeting-details">
    <span class="meeting-day">This Wednesday</span>
    <span class="meeting-time">8:40am</span>
    <span class="meeting-place">in the Multi Purpose Room</span>
  </p>

  <svg class="calendar" viewBox="0 530 848 340" width="848" height="340" aria-label="September 2013 calendar with Wednesday the 18th circled">
    <text x="417" y="567" text-anchor="middle" fill="var(--ink)"><tspan class="month">September</tspan><tspan class="year" dx="8">2013</tspan></text>

    <g class="weekdays" text-anchor="end" fill="var(--ink)">
      <text class="weekday" x="272" y="644">Monday</text>
      <text class="weekday" x="272" y="679">Tuesday</text>
      <text class="weekday" x="272" y="714">Wednesday</text>
      <text class="weekday" x="272" y="749">Thursday</text>
      <text class="weekday" x="272" y="784">Friday</text>
      <text class="weekday" x="272" y="819">Saturday</text>
      <text class="weekday" x="272" y="854">Sunday</text>
    </g>

    <g class="dates" text-anchor="middle" fill="var(--ink)">
      <text class="date" x="309" y="855">1</text>

      <text class="date" x="377" y="644">2</text>
      <text class="date" x="377" y="679">3</text>
      <text class="date" x="377" y="714">4</text>
      <text class="date" x="377" y="749">5</text>
      <text class="date" x="377" y="784">6</text>
      <text class="date" x="377" y="819">7</text>
      <text class="date" x="377" y="855">8</text>

      <text class="date" x="448" y="644">9</text>
      <text class="date" x="448" y="679">10</text>
      <text class="date" x="448" y="714">11</text>
      <text class="date" x="448" y="749">12</text>
      <text class="date" x="448" y="784">13</text>
      <text class="date" x="448" y="819">14</text>
      <text class="date" x="448" y="855">15</text>

      <text class="date" x="517" y="644">16</text>
      <text class="date" x="517" y="679">17</text>
      <text class="date" x="517" y="714">18</text>
      <text class="date" x="517" y="749">19</text>
      <text class="date" x="517" y="784">20</text>
      <text class="date" x="517" y="819">21</text>
      <text class="date" x="517" y="855">22</text>

      <text class="date" x="588" y="644">23</text>
      <text class="date" x="588" y="679">24</text>
      <text class="date" x="588" y="714">25</text>
      <text class="date" x="588" y="749">26</text>
      <text class="date" x="588" y="784">27</text>
      <text class="date" x="588" y="819">28</text>
      <text class="date" x="588" y="855">29</text>

      <text class="date" x="659" y="644">30</text>
    </g>

    <path class="date-marker" d="M500 690 C 510 684, 535 684, 539 700 C 543 718, 525 728, 512 726 C 496 724, 491 710, 496 698 C 498 693, 502 690, 506 689" fill="none" stroke="var(--marker-red)" stroke-width="3.5" stroke-linecap="round"/>
  </svg>

  <p class="welcome">All Welcome!</p>
</main>
</body>
</html>
```